New Flyer Design Project

Please see attached word Document

Target Market(s)

Property Investors, home owners

Requirements
Must have
• whats detailed in attached word document

```html
<!DOCTYPE html>
<html lang="en">
<head>
<meta charset="utf-8">
<title>Strong Loans Flyer</title>
<link href="https://fonts.googleapis.com/css2?family=Oswald:wght@400;500;700&family=Open+Sans:wght@400;600;700&display=swap" rel="stylesheet">
<style>
  :root {
    --red: #d9232d;
    --red-dark: #a8141c;
    --ink: #1b1b1b;
    --white: #ffffff;
    --text: #333333;
  }
  * { margin: 0; padding: 0; box-sizing: border-box; }
  html, body { width: 900px; height: 1200px; overflow: hidden; background: var(--white); }
  .flyer { position: relative; width: 900px; height: 1200px; overflow: hidden; font-family: "Open Sans", sans-serif; color: var(--white); }
  .backdrop { position: absolute; inset: 0; }
  .brand { position: absolute; left: 50px; top: 70px; display: flex; align-items: center; gap: 14px; font-family: "Oswald", sans-serif; font-weight: 500; font-size: 40px; letter-spacing: 1px; }
  .brand-mark { width: 34px; height: 34px; background: var(--white); }
  .call { position: absolute; left: 50px; top: 215px; }
  .call-label { display: flex; align-items: center; gap: 10px; font-family: "Oswald", sans-serif; font-size: 26px; font-weight: 500; }
  .call-number { font-family: "Oswald", sans-serif; font-size: 44px; font-weight: 500; margin-top: 2px; letter-spacing: 1px; }
  .headline { position: absolute; right: 40px; top: 470px; width: 520px; text-align: right; font-family: "Oswald", sans-serif; }
  .headline-lead { font-size: 44px; font-weight: 500; line-height: 1.1; }
  .headline-main { font-size: 72px; font-weight: 700; line-height: 1.05; text-transform: uppercase; }
  .headline-sub { font-size: 29px; font-weight: 400; letter-spacing: 1px; margin-top: 4px; }
  .assess { position: absolute; left: 440px; top: 668px; font-family: "Oswald", sans-serif; }
  .assess-label { font-size: 22px; font-weight: 400; line-height: 1.2; }
  .assess-count { font-size: 32px; font-weight: 500; line-height: 1.1; color: var(--red); }
  .offer { position: absolute; left: 50px; top: 470px; width: 250px; height: 320px; background: var(--white); box-shadow: 0 4px 14px rgba(0,0,0,.25); padding: 18px 18px; color: var(--text); text-align: center; }
  .offer-free { font-family: "Oswald", sans-serif; font-size: 92px; font-weight: 700; color: var(--red); line-height: 1; }
  .offer-title { background: var(--ink); color: var(--white); font-family: "Oswald", sans-serif; font-size: 19px; font-weight: 500; padding: 4px 0; margin: 8px 0 12px; }
  .offer-text { font-size: 13px; line-height: 1.45; text-align: left; }
  .lenders { position: absolute; left: 50px; top: 872px; width: 800px; display: grid; grid-template-columns: repeat(7, 1fr); gap: 22px 22px; }
  .lender { height: 38px; border-radius: 4px; }
  .footer { position: absolute; left: 0; top: 1080px; width: 900px; padding: 0 50px; }
  .contacts { display: flex; gap: 40px; font-size: 16px; font-weight: 600; }
  .contact { display: flex; align-items: center; gap: 8px; }
  .legal { font-size: 14px; margin-top: 22px; line-height: 1.5; }
</style>
</head>
<body>
<div class="flyer">
  <svg class="backdrop" width="900" height="1200" viewBox="0 0 900 1200">
    <defs>
      <linearGradient id="photoTone" x1="0" y1="0" x2="1" y2="1">
        <stop offset="0" stop-color="#9fb3c4"/>
        <stop offset=".5" stop-color="#c8b6a4"/>
        <stop offset="1" stop-color="#5a4a44"/>
      </linearGradient>
    </defs>
    <polygon points="0,0 900,0 900,440 0,560" fill="var(--red)"/>
    <polygon points="390,0 900,0 900,420 390,488" fill="url(#photoTone)" role="img" aria-label="Photo of a smiling couple holding house keys in front of a modern home"/>
    <polygon points="0,560 900,440 900,760 0,830" fill="var(--ink)"/>
    <polygon points="0,830 900,760 900,772 0,842" fill="var(--red)"/>
    <rect x="0" y="1050" width="900" height="150" fill="var(--red)"/>
    <rect x="0" y="1050" width="900" height="12" fill="var(--red-dark)"/>
  </svg>

  <div class="brand"><span class="brand-mark"></span>Strong Loans</div>

  <div class="call">
    <div class="call-label">
      <svg width="22" height="22" viewBox="0 0 24 24"><path fill="#fff" d="M6.6 10.8a15.1 15.1 0 006.6 6.6l2.2-2.2c.3-.3.7-.4 1-.2 1.1.4 2.3.6 3.6.6.6 0 1 .4 1 1V20c0 .6-.4 1-1 1A17 17 0 013 4c0-.6.4-1 1-1h3.5c.6 0 1 .4 1 1 0 1.3.2 2.5.6 3.6.1.3 0 .7-.2 1z"/></svg>
      CALL US TODAY
    </div>
    <div class="call-number">1300 482 615</div>
  </div>

  <div class="headline">
    <div class="headline-lead">IS YOUR MORTGAGE</div>
    <div class="headline-main">In Good Shape</div>
    <div class="headline-sub">DEFENCE FORCE SPECIALIST</div>
  </div>

  <div class="assess">
    <div class="assess-label">WE ASSESS</div>
    <div class="assess-count">OVER 30 LENDERS</div>
  </div>

  <div class="offer">
    <div class="offer-free">FREE</div>
    <div class="offer-title">1 HOUR CONSULTATION</div>
    <p class="offer-text">No selling, just transparent guidance on the in's and out's of property investing along with current hot spots and an analysis of your investment property portfolio potential.</p>
  </div>

  <div class="lenders">
    <div class="lender" style="background:#f27a21"></div>
    <div class="lender" style="background:#e53b2c"></div>
    <div class="lender" style="background:#222"></div>
    <div class="lender" style="background:#2b63a8"></div>
    <div class="lender" style="background:#6b2c7a"></div>
    <div class="lender" style="background:#f2c200"></div>
    <div class="lender" style="background:#d24a1e"></div>
    <div class="lender" style="background:#1f4f8c"></div>
    <div class="lender" style="background:#2a7fc1"></div>
    <div class="lender" style="background:#d9232d"></div>
    <div class="lender" style="background:#e74c1c"></div>
    <div class="lender" style="background:#c8102e"></div>
    <div class="lender" style="background:#78b833"></div>
    <div class="lender" style="background:#c5281c"></div>
    <div class="lender" style="background:#2d6fb6"></div>
    <div class="lender" style="background:#e9a100"></div>
    <div class="lender" style="background:#1a5aa6"></div>
    <div class="lender" style="background:#1b3f7a"></div>
  </div>

  <div class="footer">
    <div class="contacts">
      <span class="contact">
        <svg width="18" height="14" viewBox="0 0 18 14"><rect x="1" y="1" width="16" height="12" fill="none" stroke="#fff" stroke-width="1.6"/><path d="M1 1l8 7 8-7" fill="none" stroke="#fff" stroke-width="1.6"/></svg>
        mark@strongloans.com.au
      </span>
      <span class="contact">
        <svg width="16" height="16" viewBox="0 0 16 16"><circle cx="8" cy="8" r="7" fill="none" stroke="#fff" stroke-width="1.6"/><path d="M1 8h14M8 1c3 3 3 11 0 14M8 1c-3 3-3 11 0 14" fill="none" stroke="#fff" stroke-width="1.2"/></svg>
        www.strongloans.com.au
      </span>
    </div>
    <p class="legal">Strong Loans ABN 12 345 678 901 ACR No. 100200 is a credit representative of Bright Harbour ACL No 300400</p>
  </div>
</div>
</body>
</html>
```